Bright Harbor Academy Brochure Design (Competition)

Create a compelling brochure design that stands out from other training and certification offerings in the training space and develop the final brochure with copy provided by the client. Our offering includes a technical component – BHA Linkway – which is a virtual ecosystem / online portal with robust capabilities for virtual events, etc. It is our unique value proposition. It’s how we’ll stand out in the marketplace. You’ll find this in the brochure map. But, the offering is first a training and certification value proposition. This is a new product offering.
The BHA Linkway portal will be a 3-D environment, which is leading edge in our space and very sophisticated looking. We need a contemporary style that reflects that forward leaning sophistication and works with the images provided. Suggest interconnectivity everywhere without always being explicit about interconnectivity.
The designer’s skills need to fall to the artistic side of the continuum rather to the layout designer side of the continuum. We want creativity; of course, the designer needs to be able to use the tools to turn the design into a brochure.
The brochure map is crafted around a 6-page brochure with cover, back, and fold out to reveal a spread. Unfortunately, it is copy heavy. I’ll continue to look for areas to thin it, but work with what you have giving air wherever you can.
The thinking behind the flow is as follows:
When the brochure is handed to someone, they will see the cover first. Then, typically, they will turn it over to look at the back. With that behavior in mind, the cover sets the stage for why people need BHA and the back cover identifies the ways people can partner with BHA. The inside spread offers the specifics. Also, if the reader opens the first fold and keeps the second fold closed, and then turns it over, the Why Partner and Why BHA are next to each other. When you craft the .pdf version, try to keep these connections in mind as you flow the pages.
We are open to an 8-page format. It will primarily be distributed as a .pdf file attached to email and/or downloaded from the website. We will print brochures for trade shows and proposal inserts, for example, and we want to keep print costs reasonable. This version of the brochure will not be used for direct mail; so, no address block is needed.
For the .pdf used for the website/email attachment, please sequence the pages: Cover – Inside left 2 – Inside center 3 – inside right page 4 – inside fold-in opposite in the inside left p5 – back page 6.
For the .pdf used for print, please sequence the pages so they support the 6-page fold in approach, if that is the design you propose. If the brochure map does not make that clear to you, please ask.
We have an existing logo and images that represent various areas in the online portal, attached. Note, we will have one more image for the online portal that will represent a virtual expo hall. Please use a placeholder image so we don’t forget to include it where appropriate.
CMYK colors
Cyan 99
Magenta 77
Yellow 4
Black 0.5
RGB Colors
Red 2
Green 79
Blue 159
CMYK colors
Cyan 57
Magenta 49
Yellow 48
Black 15
RGB Colors
Red 111
Green 111
Blue 111
Updates
Hello, designers. Everyone seems to be confused by the 6-page format. So, I've rewritten that instruction in the brochure map to help clarify. Also, I know that the brochure was copy heavy. Now that I see some designs, I have found several opportunities to cut copy and shorten some of the statements. Hopefully this will help everyone. Check the brief for the new brochure map, V3. Thank you all for playing.
Look and feel
Each slider illustrates characteristics of the customer's brand and the style your logo design should communicate.

```html
<!DOCTYPE html>
<html lang="en">
<head>
<meta charset="utf-8">
<title>Bright Harbor Academy – Back Brochure</title>
<link href="https://fonts.googleapis.com/css2?family=Montserrat:wght@200;400;500;600;700&display=swap" rel="stylesheet">
<style>
:root{
  --brand-blue:#024f9f;
  --band-blue:#0450a2;
  --bar-light:#4aa3e6;
  --bar-dark:#0b55a8;
  --panel-gray:#eeeeef;
  --ink:#3a3a3a;
  --white:#ffffff;
  --label-gray:#a9a49e;
  --page:#f8f8f8;
}
*{margin:0;padding:0;box-sizing:border-box}
html,body{width:1200px;height:1200px;overflow:hidden;background:var(--page)}
body{font-family:'Montserrat',sans-serif;position:relative}
.top-band{position:absolute;left:0;top:0;width:1200px;height:176px;background:var(--band-blue)}
.column{position:absolute;top:176px;width:400px;height:848px;overflow:hidden}
.col-tracks{left:0;background:var(--panel-gray);border-left:1px solid #d8d8d8}
.col-connect{left:400px;background:linear-gradient(180deg,#4d9ad8 0%,#2e79c2 45%,#0b55a8 100%)}
.col-ecosystem{left:800px}
.abs{position:absolute}
p{font-size:12.6px;line-height:15.6px;text-align:justify}
p b{font-weight:600}

/* tracks column */
.tracks-header{left:0;top:0;width:400px;height:110px;background:linear-gradient(180deg,#3c3c3e,#4a4a4d)}
.tracks-title{left:0;top:28px;width:400px;text-align:center;color:var(--white);font-size:24px;line-height:30px;font-weight:500}
.tracks-title b{font-weight:700}
.tracks-col .txt{left:14px;width:374px;color:var(--ink)}
.bar{left:0;width:400px;height:31px;background:linear-gradient(180deg,var(--bar-light),var(--bar-dark));color:var(--white);font-weight:600;font-size:17px;line-height:31px;text-align:center}
.track-list{list-style:none;font-size:12.6px;line-height:15.6px}
.track-list li::before{content:"-";display:inline-block;width:15px}

/* connect column */
.connect-photo{left:0;top:0;width:400px;height:224px;background:linear-gradient(180deg,#9fb3c8 0%,#6f7f92 55%,#4a5666 100%)}
.connect-title-box{left:34px;top:184px;width:332px;height:72px;background:linear-gradient(180deg,rgba(74,150,215,.85),rgba(32,108,186,.95));color:var(--white);font-weight:700;font-size:37px;line-height:60px;text-align:center}
.connect-col .txt{left:27px;width:347px;color:var(--white)}
.connect-sub{font-weight:700;font-size:12.2px;line-height:15.6px}

/* ecosystem column */
.eco-photo{left:0;top:0;width:400px;height:848px;background:linear-gradient(180deg,#6d6558 0%,#5d5248 30%,#51443d 60%,#3f3431 100%)}
.eco-title{left:26px;top:214px;width:360px;color:var(--white);font-size:31px;line-height:38px;font-weight:500}
.eco-col .txt{left:26px;width:347px;color:var(--white)}

.page-label{position:absolute;left:0;top:1068px;width:1200px;text-align:center;font-weight:200;font-size:90px;line-height:100px;color:var(--label-gray);letter-spacing:1px}
</style>
</head>
<body>
<div class="top-band"></div>

<section class="column col-tracks tracks-col">
  <div class="abs tracks-header" role="img" aria-label="Photo of professionals in a training room, dark toned"></div>
  <h1 class="abs tracks-title"><b>BHA</b> Career Track<br>Training And Certification</h1>
  <p class="abs txt" style="top:128px;text-align:left">Preparing job-ready professionals for today’s challenging workplace</p>
  <h2 class="abs bar" style="top:170px">Six Career Tracks</h2>
  <p class="abs txt" style="top:212px">Carefully crafted for workers new to the workplace, who need to brush up on skills for current responsibilities or prepare for career advancement.</p>
  <ul class="abs txt track-list" style="top:274px">
    <li>Small Business Ownership</li>
    <li>Customer Service</li>
    <li>Marketing</li>
    <li>Sales</li>
    <li>Talent Development and Human Resources</li>
    <li>Administrative Support</li>
    <li>Plus, Workplace Professional – A Certification Program</li>
  </ul>
  <p class="abs txt" style="top:398px">Focused on business and soft skill competencies directly relevant to the realities of the workplace.</p>
  <p class="abs txt" style="top:445px">Established, governed, and maintained by the BHA International Certification Standards Board.</p>
  <p class="abs txt" style="top:492px">All designed for adult learners, incorporating a wide range of techniques so learners can practice, reinforce, and validate learning.</p>
  <h2 class="abs bar" style="top:548px">Validate Job Skills Competency</h2>
  <p class="abs txt" style="top:587px">Gain prestige and career advantage. Stand out in today’s competitive marketplace with BHA Certified Professional credentials.</p>
  <p class="abs txt" style="top:650px">Make work experience count. Verify the competencies achieved through years of work experience. Or, take the certification course first to update skills and increase the odds of passing the exam.</p>
  <h2 class="abs bar" style="top:716px">Make Learning A Life-long Pursuit</h2>
  <p class="abs txt" style="top:758px">The Harbor Lifelong Learning Series is a vast training library that complements the career track programs with specialty topics, concepts and skills professionals need along the way.</p>
</section>

<section class="column col-connect connect-col">
  <div class="abs connect-photo" role="img" aria-label="3-D rendering of a virtual lounge with seating, screens and visitors"></div>
  <h1 class="abs connect-title-box">BHA Linkway</h1>
  <p class="abs txt connect-sub" style="top:280px;text-align:left">A HIGH-TECH VIRTUAL ECOSYSTEM CONNECTING ALL STAKEHOLDERS IN THE CAREER LIFE-CYCLE</p>
  <p class="abs txt" style="top:326px">A socially-engaging environment, BHA Linkway integrates career training, certification, the job marketplace, events, and creative resources in a single portal.</p>
  <p class="abs txt" style="top:405px"><b>Learners -</b> Review course offerings, register and attend classes, take exams, attend virtual events, and chat with other participants.</p>
  <p class="abs txt" style="top:467px"><b>Enterprise Buyers and Authorized Trainer Partners -</b> Purchase and access all authorized training materials, publish your training schedule, register participants, host classes and webinars, and access course evaluations and test results for your learners and customers.</p>
  <p class="abs txt" style="top:577px"><b>Employers and Recruiters -</b> Promote job vacancies, screen candidate resumes, schedule and conduct candidate interviews, and verify BHA credentials.</p>
  <p class="abs txt" style="top:639px"><b>Sponsors and Partners -</b> Participate in the 24 x 365 virtual exhibit hall, chat with prospects, promote your products and services in banner ads, ticker tapes, virtual events, and sponsored webcasts.</p>
  <p class="abs txt" style="top:718px"><b>Trainers -</b> Purchase and access all authorized training materials, conduct online classes and take full advantage of BHA resources as a community member.</p>
</section>

<section class="column col-ecosystem eco-col">
  <div class="abs eco-photo" role="img" aria-label="3-D rendering of a virtual resources center with tables and visitors"></div>
  <h1 class="abs eco-title">Explore the Ecosystem</h1>
  <p class="abs txt" style="top:272px"><b>The Lobby -</b> Visitors and registered members enter the ecosystem through a virtual lounge, then easily navigate throughout the space and network with others.</p>
  <p class="abs txt" style="top:350px"><b>Networking Zone -</b> A hub of activity. Chat informally or participate in scheduled group discussion with topic experts, colleagues, trainers, recruiters, and special guests.</p>
  <p class="abs txt" style="top:429px"><b>Learning Zone</b> – The training venue. Access the theater and classrooms for live event experiences. Integrated with the LMS, training providers securely maintain student records, learning paths, progress, and customer reports.</p>
  <p class="abs txt" style="top:522px"><b>Expo Zone</b> – A virtual trade-show. Where sponsors and partners market their products and services 24 X 365 or on a scheduled event basis.</p>
  <p class="abs txt" style="top:585px"><b>Idea Zone</b> – An online library and resource center. Visitors can read blogs and articles, view videos on-demand, and access other free content, easily downloadable from the portal.</p>
  <p class="abs txt" style="top:663px"><b>Gaming Zone</b> – The game center. Where visitors and community members play educational games, earn participation points and badges, watch the leader board, and keep track of activities.</p>
  <p class="abs txt" style="top:741px">There’s so much more to explore. We’ll host job fairs, conferences, award programs, and webcast, all available from any device, anywhere. Plus, you’ll find a skills testing center, a recruiting center, and a trainer’s hub. There’s simply nothing like it.</p>
</section>

<div class="page-label">BACK BROCHURE</div>
</body>
</html>
```